依頼詳細
配置構図、記載文言は別紙添付ファイルを参照ください。
配置バランスはあくまで基本と考えていただき、工夫してアレンジして頂いて構いませんが、表面と裏面の記載内容と順序は変更不可です。

「エアコンのしくみ」「圧縮機関連イメージ図(2つ)」「コーティング作用による修復イメージ図」は元図を参考、または利用して作成をお願いします。

一般家庭の女性(主に主婦のかた)が見ることが一番多いと思います。
見やすいのが一番ですが、あまりにシンプルになりすぎないようにしてください。
指示以外のイラストや挿絵もアイデアがあれば自由にご提案ください。

今回のものをベースに業務用サービスのチラシの作製も必要になりますので継続してお任せできる良いデザイナーの方に出会えることを期待しています。

何かわからない点があれば遠慮なく何でも聞いてください。
どうぞお力を貸してください。
よろしくお願いいたします。

記載項目
別紙にて指示。添付ファイルを参照ください。
サイズ
A4
ページ数
両面
希望イメージ
シンプル 複雑
単色 カラフル
暗い 明るい
日常 高級
遊び心 厳粛
未来的 伝統的
女性的 男性的
希望する色
納品ファイル
• 高解像度JPG (.jpg)
• イラストレーター形式 (.ai)
補足説明
業者さんからの希望で、できることならば4月末までに印刷したいので納期を少しタイトに設定します。あまりに応募数が少ない時は延長します。ご協力のほどよろしくお願いいたします。
一度にまとめてファイルを添付できなかったので、追加でaiデータを添付しようとしましたが
容量オーバーで添付できないようです。仕方ないのでPDFを添付します。

「エアコンの経年劣化と消費電力グラフ」
「エアコンの消費電力割合(円グラフ)」
「作業の流れ」(施行手順)

はこのデータから活用ください。

よろしくお願いいたします。
■ 選んだ理由

このチラシを活用する業者の方が一番お客様に伝えやすいデザインと言われたことが最終的な選定理由です。

■ 提案者全員のお礼・コメント

エアコンの室外機のコンプレッサー性能回復剤というふだん見慣れない商品のチラシ作成にご尽力いただき心から感謝申し上げます。
どれもすばらしいデザインでした。お一人しか選定できないのは心苦しい限りです。
本当にありがとうございました。

```html
<!DOCTYPE html>
<html lang="ja">
<head>
<meta charset="UTF-8">
<title>コンプレッサー性能回復剤</title>
<link href="https://fonts.googleapis.com/css2?family=Noto+Sans+JP:wght@400;500;700;900&display=swap" rel="stylesheet">
<style>
:root{
  --navy:#123a7a;
  --blue:#1f6fc9;
  --sky:#dcebf8;
  --sky-deep:#a9cbe9;
  --red:#e0261c;
  --orange:#f28a1e;
  --ink:#1d2433;
  --white:#ffffff;
  --paper:#f4f8fc;
}
*{margin:0;padding:0;box-sizing:border-box}
html,body{width:849px;height:1200px;overflow:hidden;background:var(--white)}
body{font-family:"Noto Sans JP",sans-serif;color:var(--ink)}
.flyer{position:relative;width:849px;height:1200px;overflow:hidden}

/* hero */
.hero{position:absolute;left:0;top:0;width:849px;height:430px}
.hero-photo{position:absolute;inset:0;background:linear-gradient(120deg,#eef3f8 0%,#d8e1ea 45%,#b9c6d3 100%)}
.catch{position:absolute;left:0;top:16px;background:var(--navy);color:var(--white);font-weight:700;font-size:22px;padding:8px 26px 8px 16px;clip-path:polygon(0 0,100% 0,94% 100%,0 100%)}
.title{position:absolute;left:0;top:64px;background:var(--blue);color:var(--white);font-weight:900;font-size:38px;letter-spacing:1px;padding:6px 26px 8px 16px}
.lead{position:absolute;left:10px;top:128px;width:390px;font-weight:700;font-size:17px;line-height:1.55;color:var(--ink);background:rgba(255,255,255,.8);padding:4px 8px}
.tags{position:absolute;left:16px;top:196px;display:flex;gap:8px}
.tag{background:var(--blue);color:var(--white);font-weight:700;font-size:16px;padding:4px 12px}
.price{position:absolute;left:12px;top:240px;width:400px;background:var(--white);border:2px solid var(--red);padding:2px 14px;display:flex;align-items:baseline;gap:6px;color:var(--red);font-weight:900}
.price .unit{font-size:26px}
.price .num{font-size:44px;letter-spacing:1px}
.price .tax{font-size:18px;font-weight:700}
.badge{position:absolute;right:10px;top:-14px;width:120px;height:120px;border-radius:50%;background:var(--blue);color:var(--white);display:flex;align-items:center;justify-content:center;text-align:center;font-weight:700;font-size:17px;line-height:1.3;padding-top:18px}
.power{position:absolute;right:12px;top:262px;width:232px;background:var(--white);border:2px solid var(--red);text-align:center}
.power .label{background:var(--red);color:var(--white);font-weight:700;font-size:17px;padding:2px 0}
.power .value{color:var(--red);font-weight:900;font-size:30px;line-height:1.2;padding-top:2px}
.power .value small{font-size:17px}
.power .note{font-size:10px;color:var(--ink);padding-bottom:4px}

/* section headings */
.band{position:absolute;left:0;width:849px;height:34px;background:var(--sky);border-left:8px solid var(--blue)}
.band h2{font-size:20px;font-weight:900;color:var(--navy);line-height:34px;padding-left:12px}

/* how it works */
.scheme{position:absolute;left:12px;top:490px;width:400px;height:350px;border:1px solid var(--sky-deep);background:linear-gradient(180deg,#eaf4fc 0%,#fde9e2 100%)}
.point{position:absolute;left:428px;width:410px}
.point h3{font-size:18px;font-weight:900;color:var(--navy);display:flex;align-items:center;gap:8px;border-bottom:2px solid var(--blue);padding-bottom:3px;margin-bottom:8px}
.point h3::before{content:"";width:14px;height:14px;background:var(--blue)}
.point p{font-size:15px;line-height:1.65;font-weight:500}
.point .em{color:var(--red);font-weight:700}
.share{display:flex;align-items:center;gap:10px}
.share p{flex:1}

/* graph section */
.chart{position:absolute;left:14px;top:900px;width:540px;height:290px}
.person{position:absolute;left:568px;top:900px;width:120px;height:200px;background:linear-gradient(180deg,#fde0c6,#f3b980);border-radius:60px 60px 10px 10px}
.ratio{position:absolute;left:700px;top:960px;font-size:15px;font-weight:700;line-height:2}
.ratio span{display:inline-block;width:90px}
.bubble{position:absolute;left:700px;top:1080px;width:136px;height:80px;border-radius:50%;background:#fff4c2;border:2px solid var(--orange);color:var(--navy);font-weight:900;font-size:16px;text-align:center;display:flex;align-items:center;justify-content:center;line-height:1.35}
</style>
</head>
<body>
<div class="flyer">

  <section class="hero">
    <div class="hero-photo" role="img" aria-label="住宅の外壁に設置されたエアコン室外機の写真"></div>
    <div class="catch">省エネ効果がずっと続く!</div>
    <h1 class="title">コンプレッサー性能回復剤</h1>
    <p class="lead">金属表面の修復保護作用でエアコンの心臓部である圧縮機（コンプレッサー）の性能が回復。</p>
    <div class="tags">
      <span class="tag">省エネ</span><span class="tag">電気料金削減</span><span class="tag">製品寿命の延長</span>
    </div>
    <div class="price"><span class="unit">1台</span><span class="num">5,500円</span><span class="tax">(税込)</span></div>
    <div class="badge">CO2削減に<br>貢献</div>
    <div class="power">
      <div class="label">消費電力</div>
      <div class="value">10%〜15%<small>削減</small></div>
      <div class="note">（当社実績値）</div>
    </div>
  </section>

  <div class="band" style="top:442px"><h2>【エアコンのしくみ】</h2></div>
  <div class="scheme" role="img" aria-label="室内機と室外機の間を冷媒が循環し、冷房時に熱を屋外へ運ぶエアコンのしくみ図"></div>

  <div class="point" style="top:492px">
    <h3>圧縮機はエアコンの心臓部</h3>
    <p>圧縮機（コンプレッサー）の性能が劣化すると熱をたくさん運べなくなるので圧縮機の稼働時間が多くなります。<span class="em">当然に消費電力は増加し、故障しやすくなります。</span></p>
  </div>

  <div class="point" style="top:660px">
    <h3>エアコンの電気料金の90%が圧縮機</h3>
    <div class="share">
      <p>エアコンが消費する電力の約90%が室外機の圧縮機（コンプレッサー）を動かすために使われています。</p>
      <svg width="150" height="150" viewBox="0 0 150 150" aria-label="消費電力の割合：圧縮機90%、その他10%">
        <circle cx="75" cy="75" r="70" fill="var(--blue)"/>
        <path d="M75 75 L75 5 A70 70 0 0 0 33.9 18.4 Z" fill="var(--orange)"/>
        <text x="54" y="40" font-size="11" font-weight="700" fill="#fff">その他</text>
        <text x="75" y="102" text-anchor="middle" font-size="13" font-weight="700" fill="#fff">コンプレッサー</text>
        <text x="75" y="124" text-anchor="middle" font-size="22" font-weight="900" fill="#fff">90%</text>
      </svg>
    </div>
  </div>

  <div class="band" style="top:856px"><h2>エアコンの経年劣化と消費電力グラフ</h2></div>

  <svg class="chart" viewBox="0 0 540 290" aria-label="使用年数とともに消費電力が増加するグラフ">
    <rect x="0" y="0" width="540" height="290" fill="var(--paper)"/>
    <g stroke="#c9d6e4" stroke-width="1">
      <line x1="50" y1="60" x2="520" y2="60"/><line x1="50" y1="110" x2="520" y2="110"/>
      <line x1="50" y1="160" x2="520" y2="160"/><line x1="50" y1="210" x2="520" y2="210"/>
    </g>
    <line x1="50" y1="20" x2="50" y2="255" stroke="var(--ink)" stroke-width="1.5"/>
    <line x1="50" y1="255" x2="525" y2="255" stroke="var(--ink)" stroke-width="1.5"/>
    <text x="12" y="16" font-size="11" fill="var(--ink)">消費電力</text>
    <text x="470" y="275" font-size="11" fill="var(--ink)">使用年数</text>
    <text x="60" y="24" font-size="12" font-weight="700" fill="var(--red)">劣化による電力増加</text>
    <polyline points="60,225 140,215 220,195 300,165 380,125 460,85 515,60" fill="none" stroke="var(--red)" stroke-width="3"/>
    <polyline points="60,225 140,222 220,218 300,214 380,210 460,206 515,204" fill="none" stroke="var(--blue)" stroke-width="3"/>
    <text x="400" y="230" font-size="11" fill="var(--blue)">新品時の性能</text>
    <circle cx="300" cy="165" r="22" fill="var(--orange)"/>
    <text x="300" y="169" text-anchor="middle" font-size="11" font-weight="700" fill="#fff">約1.3倍</text>
    <circle cx="460" cy="85" r="22" fill="var(--orange)"/>
    <text x="460" y="89" text-anchor="middle" font-size="11" font-weight="700" fill="#fff">約1.5倍</text>
    <text x="60" y="272" font-size="11" fill="var(--ink)">0年</text>
    <text x="290" y="272" font-size="11" fill="var(--ink)">5年</text>
    <text x="450" y="272" font-size="11" fill="var(--ink)">10年</text>
  </svg>

  <div class="person" role="img" aria-label="電気料金を心配する主婦のイラスト"></div>
  <div class="ratio">
    <div><span>購入から5〜6年</span>約1.3倍</div>
    <div><span>購入から9〜10年</span>約1.5倍</div>
  </div>
  <div class="bubble">電気料金は<br>値上げする一方</div>

</div>
</body>
</html>
```